Real Estate "For Sale" Sign for construction company

We need a sign that we can use to hang on a post and place on the road when we sell a property. The sign will be simple and will need to mainly feature our logo (files attached), as well as the words "For Sale", and then our phone number "(555) 617 3489". The sign will hang on a post that'll look something like the attached picture.

Target Market(s)

Home buyers

Industry/Entity Type

Real Estate

Font styles to use
Serif
Sans Serif

Colors
0054AA
0677BA
7BADD7
CADEEF
E8F1F8
0094D4
00A9DD
6FCCEA
C7EBF8
E9F6FB

Requirements
Must have
• For Sale & our phone number

```html
<!DOCTYPE html>
<html lang="en">
<head>
<meta charset="utf-8">
<title>For Sale Sign – Laurel Crest Properties</title>
<link rel="stylesheet" href="https://fonts.googleapis.com/css2?family=Bebas+Neue&family=Lexend:wght@400&family=Poppins:wght@600&display=swap">
<style>
  :root {
    --backdrop: #a3a3a3;
    --brand-blue-top: #0054aa;
    --brand-blue-bottom: #243b7f;
    --brand-sky: #0677ba;
    --panel-white: #ffffff;
    --phone-navy: #1a2758;
  }
  * { margin: 0; padding: 0; box-sizing: border-box; }
  html, body {
    width: 1200px;
    height: 814px;
    overflow: hidden;
    background: var(--backdrop);
  }
  .canvas {
    position: relative;
    width: 1200px;
    height: 814px;
  }
  .sale-sign {
    position: absolute;
    left: 338px;
    top: 37px;
    width: 523px;
    height: 740px;
    padding: 15px;
    background: linear-gradient(180deg, var(--brand-blue-top) 0%, var(--brand-blue-bottom) 100%);
    display: flex;
    flex-direction: column;
  }
  .brand-panel {
    height: 185px;
    background: var(--panel-white);
    display: flex;
    flex-direction: column;
    align-items: center;
    justify-content: flex-end;
    padding-bottom: 22px;
    color: var(--brand-sky);
    font-family: "Lexend", sans-serif;
    font-weight: 400;
  }
  .brand-mark {
    width: 46px;
    height: 46px;
    border-radius: 50%;
    background: var(--brand-sky);
    margin-bottom: 14px;
  }
  .brand-name {
    font-size: 38px;
    line-height: 1;
    letter-spacing: 0.5px;
  }
  .brand-tagline {
    margin-top: 10px;
    font-size: 11px;
    letter-spacing: 12px;
    margin-right: -12px;
  }
  .headline {
    flex: 1;
    display: flex;
    flex-direction: column;
    align-items: center;
    justify-content: center;
    color: var(--panel-white);
    font-family: "Bebas Neue", sans-serif;
    font-size: 245px;
    line-height: 187px;
    padding-top: 14px;
  }
  .headline span { display: block; }
  .phone-panel {
    height: 108px;
    background: var(--panel-white);
    display: flex;
    align-items: center;
    justify-content: center;
    color: var(--phone-navy);
    font-family: "Poppins", sans-serif;
    font-weight: 600;
    font-size: 54px;
    letter-spacing: -0.5px;
  }
</style>
</head>
<body>
<main class="canvas">
  <section class="sale-sign" aria-label="For sale sign">
    <header class="brand-panel">
      <div class="brand-mark" aria-hidden="true"></div>
      <div class="brand-name">Laurel Crest</div>
      <div class="brand-tagline">PROPERTIES</div>
    </header>
    <h1 class="headline"><span>FOR</span><span>SALE</span></h1>
    <footer class="phone-panel">(555) 617 3489</footer>
  </section>
</main>
</body>
</html>
```